Larkfield Wp design

We need a wordpress design that will incorporate a professional color scheme with company logo in a clean layout. The design needs to consider that this will be developed on a responsive theme. Colors are undetermined - can use different blue or red as highlight - creative use of colors will be important. Client wants a 'modern' look.

Industry/Entity Type

It Company

Font styles to use
Serif
Sans Serif

Colors

Designer to choose colors to be used in the design.

Requirements
Must have
• - Navigation: 1) Home 2) Real Estate For Sale 3) Auctions 4) About Us 5) Selling Your Property 6) Contact Us

Site will have slideshow - 1st image is attached.
Home Page Content:
My service, experience and dedication provide motivated Sellers and Buyers with a clear marketing advantage. I know that the only way to succeed in real estate is to provide more service than you can get anywhere else. And you will get that kind of service when you work with me.
I will provide you with the personal service you deserve. Put my professional image, reputation, and business ethics to work for you.

Header will have - Logo (attached) Contact Information. 2 Real Estate listing buttons on the right for "New Listings" and "Upcoming Auctions" - similar to http://www.oakmereplots.example/home

and will have 4 call to action boxes- 1) Land 2) Residential 3) Commercial 4) Auctions

Footer will have site nav, smaller logo, and association logos (attached)
Nice to have
• use of dropdown menus

```html
<!DOCTYPE html>
<html lang="en">
<head>
<meta charset="utf-8">
<title>Larkfield Realty, LLC</title>
<link rel="stylesheet" href="https://fonts.googleapis.com/css2?family=Arimo:wght@400;700&family=Tinos:wght@400;700&display=swap">
<style>
:root{
  --maroon:#6a2218;
  --navy:#3d3f6f;
  --footer:#3f4377;
  --blue:#0a78d0;
  --box:#1f4b9c;
  --red:#f00000;
  --title-red:#e01010;
  --white:#ffffff;
  --light:#e8e8ee;
}
*{margin:0;padding:0;box-sizing:border-box}
html,body{width:1134px;height:1200px;overflow:hidden}
body{background:var(--maroon);font-family:"Arimo",Arial,sans-serif;color:var(--white);position:relative}
.abs{position:absolute}

.header{left:0;top:0;width:1134px;height:135px;background:var(--maroon)}
.brand{left:102px;top:30px;display:flex;align-items:center;gap:12px}
.brand-dot{width:22px;height:22px;border-radius:50%;background:var(--navy)}
.brand-name{font-family:"Tinos",serif;font-weight:700;font-size:38px;color:var(--white);line-height:1}
.call{right:96px;top:16px;font-size:16px;text-shadow:1px 1px 1px #000}
.listing-btn{top:60px;height:44px;background:linear-gradient(#fff,#e2e2e2);border-radius:8px;box-shadow:2px 2px 3px rgba(0,0,0,.5);display:flex;align-items:center;justify-content:flex-end;padding-right:20px;font-family:"Tinos",serif;font-size:21px;color:#222}
.btn-new{left:539px;width:225px}
.btn-auction{left:800px;width:238px}
.btn-icon{position:absolute;top:-6px;width:58px;height:50px;border-radius:6px}
.btn-new .btn-icon{left:8px;background:linear-gradient(#c9a27a,#7a8a4a)}
.btn-auction .btn-icon{left:2px;width:50px;background:linear-gradient(#e33 0 22%,#dfe6ee 22%)}

.nav{left:0;top:135px;width:1134px;height:51px;background:var(--navy);border-top:1px solid #8a8cb0;border-bottom:1px solid #fff}
.nav ul{list-style:none;display:flex;position:absolute;left:102px;top:8px;align-items:center}
.nav li{font-weight:700;font-size:16px;padding:0 16px;height:33px;line-height:33px;border-right:1px solid #6a6c98}
.nav li:last-child{border-right:none}
.nav li.active{background:var(--blue);border-radius:4px;border-right:none;margin-right:16px}
.nav li.after{border-left:1px solid #6a6c98}
.dropdown{left:429px;top:185px;width:148px;height:76px;background:var(--blue);padding:8px 5px;font-size:14px}
.dropdown div{height:30px;line-height:30px;padding-left:7px}
.dropdown .current{background:var(--red);margin-top:2px}

.slider{left:106px;top:208px;width:922px;height:358px;border:2px solid #fff;background:var(--white)}
.slide-photo{position:absolute;left:0;top:0;width:918px;height:302px;background:linear-gradient(#dfe9d8 0%,#6f7d4c 40%,#5a4a3c 62%,#4c6e2e 80%,#5b7d33 100%)}
.caption{position:absolute;left:0;top:302px;width:918px;height:52px;background:var(--blue);font-family:"Tinos",serif;font-size:25px;text-shadow:1px 1px 2px #000;display:flex;justify-content:space-between;align-items:center;padding:0 18px 0 10px}
.caption .price{font-size:29px}

.welcome{left:0;top:598px;width:1134px;text-align:center;font-family:"Tinos",serif;font-size:33px;color:var(--title-red)}
.intro{left:100px;top:658px;width:934px;text-align:center;font-size:15px;line-height:21px}
.intro p+p{margin-top:21px}

.cta{top:810px;width:213px;height:181px;background:var(--box);padding:0 8px}
.cta h2{font-family:"Tinos",serif;font-weight:700;font-size:25px;text-align:center;height:46px;line-height:50px;text-shadow:1px 1px 2px #000}
.cta-photo{width:197px;height:126px}
.land{left:94px}.land .cta-photo{background:linear-gradient(#cfe0ec 0 20%,#5f7a3a 20% 40%,#9aa54a 40%,#b9b95a)}
.residential{left:338px}.residential .cta-photo{background:linear-gradient(#cfdceb 0 20%,#9c6b55 20% 75%,#4f7a35 75%)}
.commercial{left:585px}.commercial .cta-photo{background:linear-gradient(90deg,#dfe3e8 0 25%,#8c8a80 25% 80%,#cfd4da 80%)}
.auctions{left:826px}.auctions .cta-photo{background:linear-gradient(#c7754a 0 15%,#4a4a4a 15% 55%,#d8d8d8 55%)}

.footer{left:0;top:1049px;width:1134px;height:151px;background:var(--footer)}
.foot-nav{left:101px;top:32px;font-size:14px;color:var(--light);word-spacing:1px}
.foot-nav span{margin:0 10px}
.copyright{left:100px;top:73px;font-size:14px;color:var(--light)}
.badges{left:775px;top:24px;display:flex;gap:18px;align-items:center}
.badge{width:42px;height:46px;background:#101010;border-radius:3px}
.badge.wide{width:88px;height:42px;background:#e8e8e8}
.badge.sq{width:40px;height:42px;background:#f5f5f5}
.foot-brand{left:850px;top:93px;display:flex;align-items:center;gap:8px}
.foot-brand .brand-dot{width:14px;height:14px;background:#bdbdbd}
.foot-brand .brand-name{font-size:24px;color:#d8d8d8}
</style>
</head>
<body>
<header class="header abs">
  <div class="brand abs"><span class="brand-dot"></span><span class="brand-name">Larkfield Realty, LLC</span></div>
  <div class="call abs">Call Us Today:&nbsp; Larkfield (555) 214-0187&nbsp; Larkfield (555) 318-0462</div>
  <div class="listing-btn btn-new abs"><span class="btn-icon" role="img" aria-label="House icon with new tag"></span>New Listings</div>
  <div class="listing-btn btn-auction abs"><span class="btn-icon" role="img" aria-label="Calendar icon"></span>Upcoming Auctions</div>
</header>

<nav class="nav abs">
  <ul>
    <li>Home</li>
    <li>Real Estate For Sale</li>
    <li class="active">Auctions</li>
    <li class="after">About Us</li>
    <li>Selling Your Property</li>
    <li>Contact Us</li>
  </ul>
</nav>

<section class="slider abs">
  <div class="slide-photo" role="img" aria-label="Brick ranch house with front porch among tall trees"></div>
  <div class="caption"><span>Larkfield Realty LLC</span><span class="price">$ 90,000</span></div>
</section>

<div class="dropdown abs">
  <div>Upcoming Auction</div>
  <div class="current">Past Auction</div>
</div>

<h1 class="welcome abs" style="font-weight:400">Welcome to Larkfield Realty LLC</h1>
<div class="intro abs">
  <p>My service, experience and dedication provide motivated Sellers and Buyers with a clear marketing advantage. I know that the only way to succeed in real estate is to provide more service than you can get anywhere else. And you will get that kind of service when you work with me.</p>
  <p>I will provide you with the personal service you deserve. Put my professional image, reputation, and business ethics to work for you.</p>
</div>

<div class="cta land abs"><h2>Land</h2><div class="cta-photo" role="img" aria-label="Open fenced pasture land"></div></div>
<div class="cta residential abs"><h2>Residential</h2><div class="cta-photo" role="img" aria-label="Two-story brick family home"></div></div>
<div class="cta commercial abs"><h2>Commercial</h2><div class="cta-photo" role="img" aria-label="Modern commercial office building"></div></div>
<div class="cta auctions abs"><h2>Auctions</h2><div class="cta-photo" role="img" aria-label="Crowd gathered at a live auction"></div></div>

<footer class="footer abs">
  <div class="foot-nav abs">Home<span>|</span>Real Estate For Sale<span>|</span>Auctions<span>|</span>About Us<span>|</span>Selling Your Property<span>|</span>Contact Us</div>
  <div class="copyright abs">Copyright © 2014 Larkfield Realty,LLC . All rights reserved.</div>
  <div class="badges abs">
    <span class="badge" role="img" aria-label="Auctioneer association badge"></span>
    <span class="badge wide" role="img" aria-label="State auctioneers association badge"></span>
    <span class="badge sq" role="img" aria-label="Realtor membership badge"></span>
    <span class="badge sq" role="img" aria-label="Equal housing opportunity badge"></span>
  </div>
  <div class="foot-brand abs"><span class="brand-dot"></span><span class="brand-name">Larkfield Realty</span></div>
</footer>
</body>
</html>
```